Eye surgeon needs a presentation folder and a business card for his practice manager. Logo alread...

I need a folder to put papers in when I am scheduling patients for surgery. The information is general, such as costs, consent forms etc. The folder is designed to give the patient these papers in a neat manner. The cover of the folder needs to use my brand and perhaps create some interest when it is sitting on their kitchen bench with visitors and family. I'll attach a typical template for a folder. It needs to be stylish, classic and professional, as I am about to operate on the person's eye. <br/>I would like my logo included. I'll also attach a photo which is on my website which might work to wrap around the folder. The website address is raybelford.com.au and you can see the way the image is used there on most of the pages as a banner. My profile photo could possibly used as well. Perhaps on the back, but if it looks strange then that is not necessary. The contact information need not be on the folder. Just Dr Ray Belford, Ophthalmic Surgeon. Finally, our brand slogan is. "The world's a beautiful place, see it clearly". This could also be on it. Again, this all needs to be professional looking. <br/>I've attached all our previous design jobs, 2 profile pictures, and the image that I think would work. Please also look at the website. <br/><br/>The second part of the project is to create a business card for my practice manager. Her name is Miriam Holtby<br/>It should include<br/>Miriam Holtby (BCom)<br/>Practice Manager for Dr Ray Belford<br/>Ophthalmic Surgeon <br/><br/>Then all the details which are on our current business card<br/><br/><br/><br/><br/>

Contact Information for Business Card

Just match the business cards I already have, but use the details above

Colors

Designer to choose colors to be used in the design.

```html
<!DOCTYPE html>
<html lang="en">
<head>
<meta charset="utf-8">
<title>Dr Ray Belford – Presentation Folder</title>
<link href="https://fonts.googleapis.com/css2?family=Ubuntu:wght@500&family=Open+Sans:wght@400;600&family=Roboto:wght@700&display=swap" rel="stylesheet">
<style>
  :root {
    --brand-blue: #1a7cc4;
    --brand-blue-deep: #0e62a6;
    --brand-blue-light: #2b9bdc;
    --band-white: #ffffff;
    --band-grey: #d9dadc;
    --silver-light: #f2f2f2;
    --silver-dark: #8e9095;
    --stage: #e6e6e6;
    --text-white: #ffffff;
  }
  * { margin: 0; padding: 0; box-sizing: border-box; }
  html, body { width: 1200px; height: 847px; overflow: hidden; }
  body {
    background: var(--stage);
    position: relative;
    font-family: "Open Sans", sans-serif;
  }
  .folder-spread {
    position: absolute;
    left: 100px;
    top: 70px;
    width: 1000px;
    height: 707px;
    display: flex;
    box-shadow: 0 10px 30px rgba(0,0,0,0.18);
  }
  .panel {
    position: relative;
    width: 500px;
    height: 707px;
    overflow: hidden;
  }
  .panel svg.panel-art { position: absolute; inset: 0; }

  /* wordmark */
  .wordmark { position: absolute; display: flex; align-items: center; gap: 12px; }
  .wordmark-dot { border-radius: 50%; flex: none; }
  .wordmark-name {
    font-family: "Ubuntu", sans-serif;
    font-weight: 500;
    line-height: 1;
  }
  .wordmark-role {
    font-family: "Open Sans", sans-serif;
    font-weight: 600;
    font-size: 10px;
    line-height: 1.2;
    margin-top: 4px;
  }
  .wordmark-quals {
    font-family: "Open Sans", sans-serif;
    font-weight: 400;
    font-size: 8px;
    line-height: 1.2;
  }

  /* back cover */
  .back-cover .portrait {
    position: absolute;
    left: 160px;
    top: 418px;
    width: 196px;
    height: 176px;
    background: #fff;
    padding: 5px;
    box-shadow: 0 1px 3px rgba(0,0,0,0.2);
  }
  .back-cover .portrait-fill {
    width: 100%;
    height: 100%;
    background: linear-gradient(135deg, #bcd6c9 0%, #e9e2da 45%, #c99a82 70%, #2f3038 100%);
  }
  .back-cover .wordmark { left: 48px; top: 616px; }
  .back-cover .wordmark-dot { width: 44px; height: 44px; background: var(--brand-blue); }
  .back-cover .wordmark-name { font-size: 28px; color: var(--brand-blue-deep); }
  .back-cover .wordmark-role,
  .back-cover .wordmark-quals { color: #3b4a58; }

  /* front cover */
  .front-cover .wordmark { left: 70px; top: 60px; }
  .front-cover .wordmark-dot { width: 48px; height: 48px; background: var(--text-white); }
  .front-cover .wordmark-name { font-size: 31px; color: var(--text-white); }
  .front-cover .wordmark-role,
  .front-cover .wordmark-quals { color: var(--text-white); }
  .front-cover .slogan {
    position: absolute;
    left: 0;
    width: 500px;
    top: 372px;
    text-align: center;
    font-family: "Roboto", sans-serif;
    font-weight: 700;
    font-size: 25px;
    line-height: 1.3;
    color: var(--text-white);
    text-shadow: 0 2px 4px rgba(0,0,0,0.45);
  }
</style>
</head>
<body>
  <div class="folder-spread">

    <section class="panel back-cover">
      <svg class="panel-art" width="500" height="707" viewBox="0 0 500 707">
        <defs>
          <radialGradient id="backBlue" cx="0.55" cy="0.45" r="0.75">
            <stop offset="0" stop-color="var(--brand-blue-light)"/>
            <stop offset="1" stop-color="var(--brand-blue-deep)"/>
          </radialGradient>
          <linearGradient id="backBand" x1="0" y1="0" x2="1" y2="0">
            <stop offset="0" stop-color="var(--band-grey)"/>
            <stop offset="0.5" stop-color="var(--band-white)"/>
            <stop offset="1" stop-color="var(--band-grey)"/>
          </linearGradient>
        </defs>
        <rect width="500" height="707" fill="url(#backBlue)"/>
        <path d="M0 610 Q 250 575 500 520 L 500 707 L 0 707 Z" fill="url(#backBand)"/>
      </svg>
      <div class="portrait">
        <div class="portrait-fill" role="img" aria-label="Portrait photograph of the surgeon in a dark jacket and checked shirt"></div>
      </div>
      <div class="wordmark">
        <span class="wordmark-dot"></span>
        <div>
          <div class="wordmark-name">Dr Ray Belford</div>
          <div class="wordmark-role">Ophthalmic Surgeon</div>
          <div class="wordmark-quals">MBBS (Hons) MMed FRANZCO</div>
        </div>
      </div>
    </section>

    <section class="panel front-cover">
      <svg class="panel-art" width="500" height="707" viewBox="0 0 500 707">
        <defs>
          <radialGradient id="frontBlue" cx="0.55" cy="0.3" r="0.8">
            <stop offset="0" stop-color="var(--brand-blue-light)"/>
            <stop offset="1" stop-color="var(--brand-blue)"/>
          </radialGradient>
          <linearGradient id="silverBand" x1="0" y1="0" x2="1" y2="0">
            <stop offset="0" stop-color="var(--silver-dark)"/>
            <stop offset="0.35" stop-color="var(--silver-light)"/>
            <stop offset="0.65" stop-color="var(--silver-dark)"/>
            <stop offset="1" stop-color="var(--silver-light)"/>
          </linearGradient>
          <linearGradient id="sunsetSea" x1="0" y1="0" x2="0" y2="1">
            <stop offset="0" stop-color="#d99a3e"/>
            <stop offset="0.3" stop-color="#efb24a"/>
            <stop offset="0.42" stop-color="#6b5236"/>
            <stop offset="0.7" stop-color="#2b2722"/>
            <stop offset="1" stop-color="#1b1a19"/>
          </linearGradient>
          <linearGradient id="frontBand" x1="0" y1="0" x2="1" y2="0">
            <stop offset="0" stop-color="var(--band-white)"/>
            <stop offset="1" stop-color="var(--band-grey)"/>
          </linearGradient>
        </defs>
        <rect width="500" height="707" fill="url(#frontBlue)"/>
        <path d="M0 205 Q 230 160 500 250 L 500 707 L 0 707 Z" fill="url(#silverBand)"/>
        <g role="img" aria-label="Photograph of the sun setting over a calm ocean">
          <path d="M0 222 Q 230 180 500 266 L 500 560 Q 250 575 0 600 Z" fill="url(#sunsetSea)"/>
        </g>
        <path d="M0 600 Q 250 575 500 560 L 500 707 L 0 707 Z" fill="url(#frontBand)"/>
      </svg>
      <div class="wordmark">
        <span class="wordmark-dot"></span>
        <div>
          <div class="wordmark-name">Dr Ray Belford</div>
          <div class="wordmark-role">Ophthalmic Surgeon</div>
          <div class="wordmark-quals">MBBS (Hons) MMed FRANZCO</div>
        </div>
      </div>
      <p class="slogan">The World's a Beautiful Place,<br>See it Clearly</p>
    </section>

  </div>
</body>
</html>
```